Advertising agency needs site design

You will be designing a clean (plenty of white space) and vivid (colorful) design that is for an advertising agency named Beacon Brightly. Their current web site is located at www.BeaconBrightly.net. From there you can see their services and get a feel for the company as the site stands today.
The following are direct quotes from the client:
“I want a clean look with colors of the teal blue, deep yellow (in logo) and then a good energetic orange (deep orange - rich) should bring a good feel and enthusiasm.”
“The orange can be a nice accent color, not dominant.”
“Saw two other things I like - the website fizzlarkstudio.com was pretty cool. I liked how the top banner changed colors as you moved to different tabs. I am somewhat wanting the colors I mentioned - like the blue color we use can be lighter as long as it works with the logo. - love the zing leaves site. I want quirky, creative and clean look - fun feel but slightly sophisticated to work with the medical field.”
Beacon Brightly currently focuses on the following primary industries:
• Medical / Health Care – Currently the primary industry
• Retail Industry
• Automotive Industry
• Entertainment Industry
Primary Services
• Media Planning & Buying: Web, TV, Print, Radio
• Campaign monitoring and reporting
• Commercial Production: TV & Radio
• Strategic Planning
• Market Research
• Internet Marketing: Email, SEO, Web design / development
Primary Navigation will consist of the following:
• Home
• About Us
o History
o Principal Profile (sub nav)
o Sales Team & Partners
• Clients
• Services
• Testimonials
• Contact Us
They want the web site to act as a basis for future marketing collateral so the overall feel from the web site must be capable of translating to print and other collateral. I do not currently have a clean digital version of their logo however their logo is on the web site (beaconbrightly.net)
Target Market(s)
larger companies that are purchasing air time on television and radio. Typically in the health care industry and others described above in brief.
Industry/Entity Type
Advertising
Look and feel

```html
<!DOCTYPE html>
<html lang="en">
<head>
<meta charset="utf-8">
<title>Beacon Brightly – Advertising Agency</title>
<link href="https://fonts.googleapis.com/css2?family=Arimo:ital,wght@0,400;0,700;1,400&display=swap" rel="stylesheet">
<style>
:root{
  --page:#dfeaf0;
  --teal:#0f9fc8;
  --teal-dark:#0489b3;
  --teal-light:#20b9df;
  --navy:#0d5a84;
  --orange:#ff8a12;
  --orange-dark:#f26f00;
  --text:#555;
  --muted:#777;
  --rule:#dde3e6;
  --white:#fff;
}
*{margin:0;padding:0;box-sizing:border-box}
html,body{width:1200px;height:892px;overflow:hidden}
body{
  position:relative;
  font-family:"Arimo",Arial,sans-serif;
  color:var(--text);
  background:
    linear-gradient(180deg,#c9dde5 0,#eef5f7 150px,#f7fafb 300px,#e4edf1 443px,var(--page) 443px);
}
.abs{position:absolute}

/* Header */
.brand{left:176px;top:40px;display:flex;align-items:center;gap:8px}
.brand-dot{width:12px;height:12px;border-radius:50%;background:#f5a623}
.brand-name{font-size:21px;font-weight:700;color:var(--navy);letter-spacing:.5px;white-space:nowrap}
.tagline{left:390px;top:54px;font-size:17px;color:#4aa8cc;white-space:nowrap}
.phone{left:823px;top:52px;display:flex;align-items:center;gap:10px}
.phone-number{font-size:30px;color:var(--navy);letter-spacing:-.5px}
.phone-number span{color:var(--teal)}

/* Navigation */
.nav{left:141px;top:103px;width:918px;height:38px;border-radius:7px;
  background:linear-gradient(180deg,#3ccbeb 0,#14a8d4 50%,#0c95c2 100%);
  box-shadow:0 3px 6px rgba(0,80,110,.2);border:1px solid #0b89b3}
.nav-list{list-style:none;position:absolute;left:0;top:0;height:100%}
.nav-item{position:absolute;top:0;height:36px;line-height:36px;font-size:13.5px;font-weight:700;color:var(--white);white-space:nowrap}
.nav-item.sep::before{content:"";position:absolute;left:-10px;top:5px;width:1px;height:26px;background:rgba(255,255,255,.35)}
.nav-home{left:38px;width:56px;height:45px;top:0;text-align:center;border-radius:0 0 3px 3px;
  background:linear-gradient(180deg,#ffa640,var(--orange-dark))}
.search{right:8px;top:7px;width:186px;height:22px;border-radius:11px;background:var(--white);overflow:hidden;display:flex}
.search-field{flex:1;font-size:11.5px;color:#999;padding:4px 14px}
.search-btn{width:32px;background:linear-gradient(180deg,#ffa640,var(--orange-dark));display:flex;align-items:center;justify-content:center}

/* Hero */
.hero-photo{left:183px;top:159px;width:417px;height:284px;border-radius:40px 40px 0 0;
  background:linear-gradient(180deg,#cfe2ec,#9fc7dc 50%,#86b6d0)}
.hero-title{left:641px;top:192px;font-size:50px;font-weight:700;letter-spacing:-.5px;
  background:linear-gradient(180deg,#1cb9e0,#0a8fc0);-webkit-background-clip:text;background-clip:text;color:transparent}
.hero-text{left:641px;top:262px;width:340px;font-size:13px;line-height:18.8px;color:#555}
.btn-more{left:818px;top:358px;width:136px;height:40px;border-radius:9px;border:1px solid #e8720a;
  background:linear-gradient(180deg,#ffc07a 0,#ff9a2a 48%,#f57f00 52%,#ff8f14);
  color:var(--white);font-size:21px;font-weight:700;text-align:center;line-height:38px;
  box-shadow:0 8px 8px -4px rgba(0,0,0,.15)}
.arrow{width:56px;height:56px;border-radius:50%;background:radial-gradient(circle at 45% 35%,#fff,#dfe3e5 70%,#c9cfd2);
  box-shadow:0 2px 4px rgba(0,0,0,.15);display:flex;align-items:center;justify-content:center}
.arrow-prev{left:142px;top:273px}
.arrow-next{left:1000px;top:273px}

/* Content band */
.content{left:0;top:443px;width:1200px;height:288px;
  background:linear-gradient(180deg,#e9eef1 0,#fff 22px,#fff 240px,#f1f4f5 288px);border-top:1px solid #fff}
.col-title{font-size:23px;font-weight:700;color:var(--orange);display:flex;align-items:center;gap:10px}
.col-news{left:133px;top:463px;width:236px}
.col-services{left:422px;top:463px}
.col-testimonials{left:806px;top:463px;width:250px}
.news-item{font-size:11px;line-height:17px;color:var(--muted);padding:8px 8px;border-bottom:1px solid var(--rule);white-space:nowrap}
.news-item:last-child{border-bottom:0}
.news-item b{font-weight:700;color:#666}
.news-item i{color:var(--teal-dark)}
.news-list{margin-top:2px}
.service-list{list-style:none;margin:10px 0 0 17px;font-size:11.5px;line-height:16.9px;color:var(--teal)}
.service-list li::before{content:"▪ ";color:var(--teal)}
.service-list li.group{margin-left:-7px;font-weight:700;color:var(--teal-dark)}
.service-list li.group::before{content:""}
.quote{margin:18px 0 0 5px;font-size:11.5px;line-height:17px;color:#666}
.quote-mark{left:789px;top:500px;font-size:90px;color:#e3ebef;font-family:Georgia,serif;line-height:1}
.cite{margin-top:18px;text-align:right;font-size:11.5px;line-height:17px;font-style:italic;color:var(--teal-dark)}
.divider{top:480px;width:2px;height:220px;background:linear-gradient(180deg,transparent,#eef1f2 30%,#eef1f2 70%,transparent)}

/* Footer */
.footer{left:141px;top:731px;width:918px;height:104px;border-radius:0 0 16px 16px;
  background:linear-gradient(180deg,#14afd6,#0291bd)}
.foot-title{top:22px;font-size:22px;font-weight:700;color:#4fcdef}
.news-form{left:26px;top:55px;width:225px;height:22px;border-radius:11px;background:var(--white);display:flex;overflow:hidden}
.news-field{flex:1;font-size:11.5px;color:#888;padding:4px 15px}
.news-btn{width:66px;background:linear-gradient(180deg,#ffa640,var(--orange-dark));color:var(--white);font-size:11.5px;line-height:22px;text-align:center}
.social{left:371px;top:52px;display:flex;gap:7px}
.social-box{width:30px;height:30px;border-radius:4px;border:1px solid rgba(255,255,255,.6)}
.contact-list{left:671px;top:53px;font-size:12px;line-height:14px;color:var(--white)}
.copyright{left:0;top:851px;width:1200px;text-align:center;font-size:12px;color:#888}
</style>
</head>
<body>

<header>
  <div class="abs brand"><span class="brand-dot"></span><span class="brand-name">Beacon Brightly</span></div>
  <p class="abs tagline">Sed ut perspiciatis unde omnis iste natus</p>
  <div class="abs phone">
    <svg width="36" height="26" viewBox="0 0 36 26"><path d="M2 8c0-5 32-5 32 0v3h-8V8H10v3H2z" fill="#5bbad9"/><rect x="7" y="11" width="22" height="14" rx="3" fill="#5bbad9"/><circle cx="18" cy="18" r="4" fill="#fff"/></svg>
    <div class="phone-number"><span>1000</span> 000.000</div>
  </div>
</header>

<nav class="abs nav">
  <ul class="nav-list">
    <li class="nav-item nav-home">Home</li>
    <li class="nav-item sep" style="left:116px">About Us</li>
    <li class="nav-item sep" style="left:214px">Clients</li>
    <li class="nav-item sep" style="left:299px">Services</li>
    <li class="nav-item sep" style="left:392px">Testimonials</li>
    <li class="nav-item sep" style="left:506px">Contact Us</li>
  </ul>
  <div class="abs search">
    <span class="search-field">Search</span>
    <span class="search-btn"><svg width="14" height="14" viewBox="0 0 14 14"><circle cx="5" cy="5" r="3.5" fill="none" stroke="#fff" stroke-width="2"/><path d="M7.5 7.5L12 12" stroke="#fff" stroke-width="2.5" stroke-linecap="round"/></svg></span>
  </div>
</nav>

<section class="hero">
  <div class="abs hero-photo" role="img" aria-label="Photo of a medical team in light blue scrubs standing together"></div>
  <h1 class="abs hero-title">Medical care</h1>
  <p class="abs hero-text">Sed ut perspiciatis unde omnis iste natus error sit voluptatem accusantium doloremque laudantium, totam rem aperiam, eaque ipsa quae ab illo inventore veritatis et quasi architecto beatae vitae dicta sunt explicabo.</p>
  <div class="abs btn-more">read more</div>
  <div class="abs arrow arrow-prev"><svg width="24" height="28" viewBox="0 0 24 28"><path d="M18 3L6 14l12 11" fill="none" stroke="#0fa3cf" stroke-width="6" stroke-linecap="round" stroke-linejoin="round"/></svg></div>
  <div class="abs arrow arrow-next"><svg width="24" height="28" viewBox="0 0 24 28"><path d="M6 3l12 11L6 25" fill="none" stroke="#0fa3cf" stroke-width="6" stroke-linecap="round" stroke-linejoin="round"/></svg></div>
</section>

<main class="abs content"></main>
<div class="abs divider" style="left:395px"></div>
<div class="abs divider" style="left:770px"></div>

<section class="abs col-news">
  <h2 class="col-title" style="margin-left:8px"><svg width="46" height="36" viewBox="0 0 46 36"><rect x="1" y="3" width="44" height="32" rx="2" fill="#f2f2f2" stroke="#999"/><rect x="6" y="8" width="16" height="4" fill="#888"/><rect x="6" y="16" width="34" height="2" fill="#bbb"/><rect x="6" y="21" width="34" height="2" fill="#bbb"/><rect x="6" y="26" width="34" height="2" fill="#bbb"/></svg>News</h2>
  <div class="news-list">
    <p class="news-item"><b>11.02.2011</b> - lorem ipsum dolor sit amet<br>consectetur adipisicing... <i>read more</i></p>
    <p class="news-item"><b>11.02.2011</b> - lorem ipsum dolor sit amet<br>consectetur adipisicing... <i>read more</i></p>
    <p class="news-item"><b>11.02.2011</b> - lorem ipsum dolor sit amet<br>consectetur adipisicing... <i>read more</i></p>
    <p class="news-item"><b>11.02.2011</b> - lorem ipsum dolor sit amet<br>consectetur adipisicing... <i>read more</i></p>
  </div>
</section>

<section class="abs col-services">
  <h2 class="col-title"><svg width="44" height="40" viewBox="0 0 44 40"><circle cx="16" cy="16" r="11" fill="none" stroke="#9aa4a8" stroke-width="6" stroke-dasharray="4 3"/><circle cx="16" cy="16" r="5" fill="#c5cbce"/><circle cx="32" cy="30" r="7" fill="none" stroke="#9aa4a8" stroke-width="4" stroke-dasharray="3 2"/></svg>Services</h2>
  <ul class="service-list">
    <li>Medical / Health Care</li>
    <li>Retail Industry</li>
    <li>Automotive Industry</li>
    <li>Entertainment Industry</li>
    <li class="group">Primary Services</li>
    <li>Media Planning &amp; Buying: Web, TV, Print, Radio</li>
    <li>Campaign monitoring and reporting</li>
    <li>Commercial Production: TV &amp; Radio</li>
    <li>Strategic Planning</li>
    <li>Market Research</li>
    <li>Internet Marketing: Email, SEO, Web design / development</li>
  </ul>
</section>

<div class="abs quote-mark">“</div>
<section class="abs col-testimonials">
  <h2 class="col-title"><svg width="46" height="38" viewBox="0 0 46 38"><ellipse cx="17" cy="14" rx="16" ry="12" fill="#2c9fe0"/><ellipse cx="29" cy="22" rx="15" ry="11" fill="#7cc63a"/><path d="M34 31l6 6-1-8z" fill="#7cc63a"/></svg>Testimonials</h2>
  <p class="quote">"In the advertising world, I felt like a sheep among wolves. Beacon Brightly put me on a path that not only saved me money, but increased sales to my ideal target market. I would advise anyone to take advantage of Beacon Brightly's market knowledge, media connections and select demographic experience."</p>
  <p class="cite">RT Halvorsen, Owner<br>Marlow's &amp; RT's Lanes</p>
</section>

<footer class="abs footer">
  <h3 class="abs foot-title" style="left:27px">Newsletter</h3>
  <div class="abs news-form"><span class="news-field">e-mail address</span><span class="news-btn">subscribe</span></div>
  <h3 class="abs foot-title" style="left:371px">Find us on</h3>
  <div class="abs social">
    <span class="social-box" role="img" aria-label="Chirper" style="background:#5cc8ea"></span>
    <span class="social-box" role="img" aria-label="Friendbook" style="background:#3b5b98"></span>
    <span class="social-box" role="img" aria-label="Clipstream" style="background:#c4302b"></span>
    <span class="social-box" role="img" aria-label="Feedline" style="background:#f26f1a"></span>
  </div>
  <h3 class="abs foot-title" style="left:667px">Contact details</h3>
  <p class="abs contact-list">Phone:<br>Address:<br>Email:</p>
</footer>

<p class="abs copyright">All rights reserved...</p>

</body>
</html>
```